■依頼の目的/概要
ピッツェリア(ナポリピッツァ専門店)の店頭に並ぶ商品用のPOPのデザインをお願いします。

■依頼詳細
ピッツェリア(ナポリピッツァ専門店)に並ぶ商品1点のデザインをお願いします。
夏物商品の紹介なので、締め切りが早くて恐縮です。
欲しい内容は
「4色スムージー」
「4色の内訳は、グリーン、パープル、イエロー、ブラック」
それぞれの原料と効能は
「グリーン
・野菜たっぷり&おなかの調子を整える!
・アボカド、小松菜、セロリ、その他」
「パープル
・ポリフェノール&プロアントシアニンで、ダイエット効果!血行促進!コラーゲン生成促進。
・4種のベリー(ブルーベリー、ラズベリー、クランベリー、ストロベリー)、豆乳、その他」
「イエロー
・美肌サポート!&アンチエイジング!
・マンゴー、チアシード(スーパーフード)、ココナツウォーター、その他」
「ブラック
・ビタミン豊富&整腸作用!DHA!低GI!
・ゴマ、豆乳、アガベシロップ(スーパーフード)、その他」
「各500円」価格は税込みですが、特にその表記は必要ないです。
「上手に効能をPRする」
「ランチタイムは、ピザをたのんだお客様には100円引き(400円)で提供します」
商品画像(添付の物ですが、ほかに”こういう構図のものが欲しい”など指定があれば、撮影し直すことも可能)
文言については、改変まったくokです。むしろ、素敵な表現を考えていただけるとありがたいです。原材料はそれぞれその他、と書いてあるように、具体的に書いてある物以外にも使用しています。
A4片面で印刷、ラミネート処理して店内に置いたり掲示したりする予定です。

■重視する点
オシャレであること。美味しそうであること。
ターゲットは30台~40台の女性。
photoshopデータで納品だとありがたいです。PDFやjpgでもok。

その他何かご不明な点がございましたら、お気軽にご質問下さい。
よろしくお願いいたします。
背景の白い商品画像を追加しました。
画質向上のため、写真を差し替えました。
たくさんのご提案をいただき、誠にありがとうございました。
7/13に社内選考を行う予定です。しばらくお待ち下さい。

大変魅力的なご提案が多かったため、選考には大変苦慮しましたが、
・女性からの支持が多かった点
・こちらの要望をしっかりくみ取っていただけた点
・全体的な華やかさ
等から、今回は当選を決めさせていただきました。
とても素敵なプランを採用でき、大変満足しております。

このたびは、大変魅力的なご提案を数多くいただき、ありがとうございました。正直大変目移りしてしまい、最終的に決まるまで二転三転したりしました。今回当選とさせていただかなかった方とも、またどこかでお仕事を依頼申し上げられたら幸いです。今後ともよろしくお願い申し上げます。

```html
<!DOCTYPE html>
<html lang="ja">
<head>
<meta charset="utf-8">
<title>4色スムージー</title>
<link rel="stylesheet" href="https://fonts.googleapis.com/css2?family=Kaushan+Script&family=M+PLUS+Rounded+1c:wght@500;800&family=Mochiy+Pop+One&display=swap">
<style>
:root{
  --paper:#ffffff;
  --ink:#3a3a3a;
  --yellow:#f2b705;
  --purple:#8b3f86;
  --purple-soft:#b2548e;
  --green:#4a9a2f;
  --green-soft:#8fb14a;
  --black:#2b2b2b;
  --pink:#e8437a;
  --red:#e2322f;
  --circle:#f7f3ec;
}
*{margin:0;padding:0;box-sizing:border-box}
html,body{width:849px;height:1200px;overflow:hidden;background:var(--paper)}
.poster{position:relative;width:849px;height:1200px;overflow:hidden;background:var(--paper);color:var(--ink);font-family:"M PLUS Rounded 1c",sans-serif}
.top-band{position:absolute;left:0;top:0;width:100%;height:14px;
  background:repeating-linear-gradient(90deg,#f2b705 0 34px,#8b3f86 34px 68px,#4a9a2f 68px 102px,#2b2b2b 102px 136px,#e8437a 136px 170px)}
.title{position:absolute;font-family:"Kaushan Script",cursive;line-height:.95;font-size:58px;font-weight:400;white-space:nowrap;z-index:2}
.title small{display:block;font-size:44px;padding-left:22px}
.title-yellow{left:25px;top:40px;color:var(--yellow)}
.title-purple{left:385px;top:205px;color:var(--purple)}
.title-green{left:410px;top:665px;color:var(--green)}
.title-black{left:250px;top:838px;color:var(--black)}
.mark{display:inline-block;width:22px;height:22px;border-radius:50%;margin-right:8px;vertical-align:middle}
.glass{position:absolute;z-index:1}
.glass-yellow{left:110px;top:225px;width:235px;height:225px}
.glass-purple{left:560px;top:335px;width:230px;height:205px}
.glass-black{left:85px;top:610px;width:240px;height:220px}
.glass-green{left:525px;top:790px;width:240px;height:200px}
.copy{position:absolute;font-size:14px;line-height:1.45;font-weight:500;z-index:2}
.copy .lead{font-weight:800;font-size:15px;white-space:nowrap}
.copy .hit{font-family:"Mochiy Pop One",sans-serif;font-size:24px;line-height:1.3;white-space:nowrap}
.copy ul{list-style:none;margin-top:4px;font-size:12.5px}
.copy-yellow{left:290px;top:58px;width:240px}
.copy-yellow .hit{color:var(--pink)}
.copy-purple{left:530px;top:50px;width:305px}
.copy-purple .hit{color:var(--red)}
.copy-black{left:50px;top:460px;width:270px}
.copy-black .hit{color:var(--pink)}
.copy-green{left:565px;top:552px;width:260px}
.copy-green .hit{color:var(--green)}
.price-badge{position:absolute;left:345px;top:430px;width:170px;height:170px;border-radius:50%;background:var(--circle);
  display:flex;flex-direction:column;align-items:center;justify-content:center;text-align:center;font-weight:800}
.price-badge .name{font-size:18px}
.price-badge .price{font-family:"Mochiy Pop One",sans-serif;font-size:26px;line-height:1.1}
.price-badge .price span{font-size:16px}
.price-badge .note{font-size:10.5px;line-height:1.35;margin-top:4px;font-weight:500}
.price-badge .off{font-family:"Mochiy Pop One",sans-serif;font-size:16px;color:var(--red)}
.fruit-border{position:absolute;left:0;top:900px;width:849px;height:300px}
</style>
</head>
<body>
<main class="poster">
  <div class="top-band"></div>

  <svg class="fruit-border" viewBox="0 0 849 300" preserveAspectRatio="none" role="img" aria-label="水彩風のフルーツと野菜のイラスト:マンゴー、ココナツ、ブルーベリー、葉、イチゴ、アボカド">
    <defs>
      <linearGradient id="fruitGrad" x1="0" x2="1" y1="0" y2="0">
        <stop offset="0" stop-color="#f2a23a"/>
        <stop offset=".3" stop-color="#b8a36a"/>
        <stop offset=".5" stop-color="#5b6fae"/>
        <stop offset=".7" stop-color="#6f9a4a"/>
        <stop offset="1" stop-color="#c9534a"/>
      </linearGradient>
    </defs>
    <path d="M0 110 Q120 30 240 90 Q340 60 430 90 Q560 10 660 70 Q760 20 849 60 L849 300 L0 300 Z" fill="url(#fruitGrad)" opacity=".75"/>
  </svg>

  <h2 class="title title-yellow">Yellow<small>Smoothie</small></h2>
  <div class="copy copy-yellow">
    <p class="lead">美肌サポート!&amp;</p>
    <p class="hit">アンチエイジング!</p>
    <ul><li>・マンゴー</li><li>・チアシード(スーパーフード)</li><li>・ココナツウォーター</li><li>・その他</li></ul>
  </div>
  <svg class="glass glass-yellow" viewBox="0 0 235 225" preserveAspectRatio="none" role="img" aria-label="イエロースムージーのグラス写真">
    <defs><linearGradient id="gY" x1="0" y1="0" x2="0" y2="1"><stop offset="0" stop-color="#fbd44a"/><stop offset="1" stop-color="#ef9b12"/></linearGradient></defs>
    <path d="M15 0 Q5 180 55 212 Q117 232 180 212 Q230 180 220 0 Z" fill="url(#gY)"/>
  </svg>

  <div class="copy copy-purple">
    <p class="lead">ポリフェノール&amp;プロアントシアニンで、</p>
    <p class="hit">ダイエット効果!</p>
    <p class="lead">血行促進!コラーゲン生成促進!</p>
    <ul><li>・4種のベリー(ブルーベリー、ラズベリー、</li><li>　クランベリー、ストロベリー)</li><li>・豆乳　・その他</li></ul>
  </div>
  <h2 class="title title-purple"><span class="mark" style="background:var(--purple-soft)"></span>Purple<small>Smoothie</small></h2>
  <svg class="glass glass-purple" viewBox="0 0 230 205" preserveAspectRatio="none" role="img" aria-label="パープルスムージーのグラス写真">
    <defs><linearGradient id="gP" x1="0" y1="0" x2="0" y2="1"><stop offset="0" stop-color="#c0608e"/><stop offset="1" stop-color="#8e3b6c"/></linearGradient></defs>
    <path d="M15 0 Q5 160 55 192 Q115 212 175 192 Q225 160 215 0 Z" fill="url(#gP)"/>
  </svg>

  <div class="price-badge">
    <p class="name">4色スムージー</p>
    <p class="price">各500<span>円</span></p>
    <p class="note">ランチタイム限定<br>ピザをご注文のお客様</p>
    <p class="off">100円OFF</p>
  </div>

  <div class="copy copy-black">
    <p class="lead">ビタミン豊富&amp;整腸作用!</p>
    <p class="hit">DHA!低GI!</p>
    <ul><li>・ゴマ　・豆乳</li><li>・アガベシロップ(スーパーフード)</li><li>・その他</li></ul>
  </div>
  <svg class="glass glass-black" viewBox="0 0 240 220" preserveAspectRatio="none" role="img" aria-label="ブラックスムージーのグラス写真">
    <defs><linearGradient id="gB" x1="0" y1="0" x2="0" y2="1"><stop offset="0" stop-color="#e4ded4"/><stop offset="1" stop-color="#b9b1a4"/></linearGradient></defs>
    <path d="M15 0 Q5 175 55 207 Q120 227 185 207 Q235 175 225 0 Z" fill="url(#gB)"/>
  </svg>
  <h2 class="title title-black"><span class="mark" style="background:var(--black)"></span>Black<small>Smoothie</small></h2>

  <div class="copy copy-green">
    <p class="lead">野菜たっぷり&amp;</p>
    <p class="hit">デトックス効果!</p>
    <ul><li>・アボカド　・小松菜</li><li>・セロリ　・その他</li></ul>
  </div>
  <h2 class="title title-green"><span class="mark" style="background:var(--green-soft)"></span>Green<small>Smoothie</small></h2>
  <svg class="glass glass-green" viewBox="0 0 240 200" preserveAspectRatio="none" role="img" aria-label="グリーンスムージーのグラス写真">
    <defs><linearGradient id="gG" x1="0" y1="0" x2="0" y2="1"><stop offset="0" stop-color="#b3c46a"/><stop offset="1" stop-color="#7f9a3c"/></linearGradient></defs>
    <path d="M15 0 Q5 155 55 187 Q120 207 185 187 Q235 155 225 0 Z" fill="url(#gG)"/>
  </svg>
</main>
</body>
</html>
```